Business Card Design Project

Business card design with a funky, clean, modern design. Business is an immigration consultancy. Client base will be Canadian employers wanting to hire or retain foreign workers and foreign nationals wanting to immigrate to Canada.

Full color possible, but should incorporate red/white/black as per the logo to be provided. Double sided card design.

Target Market(s)

Canadian employers looking to hire/retain staff and also foreign nationals immigrating to Canada

Industry/Entity Type

Business

Requirements
Must have
• Logo (to be provided)
Name (Marla Voskuil, Immigration Consultant)
Phone (604) 731-5562
E-mail: marla@tallowbrookmigration.example
Web: www.tallowbrookmigration.example

Nice to have
• Tag Line
Clean, modern style

```html
<!DOCTYPE html>
<html lang="en">
<head>
<meta charset="utf-8">
<title>Tallowbrook Migration – Business Card</title>
<link href="https://fonts.googleapis.com/css2?family=Cinzel:wght@700&family=Open+Sans:wght@400;600&display=swap" rel="stylesheet">
<style>
  :root {
    --page-bg: #e9e7e4;
    --card-black: #141414;
    --card-charcoal: #3a3b3d;
    --brand-red: #d3121a;
    --brand-red-deep: #8e0a0f;
    --silver-light: #f4f4f4;
    --silver-mid: #d9d9d9;
    --ink: #1e1e1e;
    --ink-soft: #3a3a3a;
    --white: #ffffff;
  }
  * { box-sizing: border-box; margin: 0; padding: 0; }
  html, body {
    width: 1200px; height: 900px; overflow: hidden;
    background: var(--page-bg);
  }
  .canvas {
    width: 1200px; height: 900px;
    display: flex; flex-direction: column;
    align-items: center; justify-content: center; gap: 44px;
  }
  .card {
    position: relative;
    width: 620px; height: 350px;
    border-radius: 28px;
    overflow: hidden;
    box-shadow: 0 10px 28px rgba(0,0,0,.25);
  }

  /* Front side */
  .card-front {
    background: linear-gradient(100deg, var(--card-black) 0%, #2b2c2e 55%, #6b6c6e 80%, #2a2a2b 100%);
  }
  .world-map {
    position: absolute; left: 0; top: 0; width: 100%; height: 78%;
    background: radial-gradient(ellipse at 40% 45%, rgba(90,92,96,.55), rgba(30,30,32,0) 70%);
  }
  .front-brand {
    position: absolute; left: 0; right: 0; top: 78px;
    display: flex; flex-direction: column; align-items: center; gap: 18px;
  }
  .brand-dot {
    width: 62px; height: 62px; border-radius: 50%;
    background: var(--brand-red);
  }
  .brand-name {
    font-family: "Cinzel", serif; font-weight: 700;
    text-transform: uppercase; text-align: center; line-height: 1.05;
  }
  .card-front .brand-name { color: var(--white); font-size: 36px; letter-spacing: 1px; }
  .red-band {
    position: absolute; left: 0; bottom: 0; width: 100%; height: 22%;
    background: linear-gradient(180deg, var(--brand-red) 0%, var(--brand-red-deep) 100%);
  }

  /* Back side */
  .card-back {
    background: linear-gradient(110deg, var(--silver-mid) 0%, var(--silver-light) 45%, #ffffff 60%, var(--silver-mid) 100%);
  }
  .back-content {
    position: absolute; left: 0; right: 0; top: 34px;
    display: flex; flex-direction: column; align-items: center;
  }
  .card-back .brand-dot { width: 40px; height: 40px; margin-bottom: 10px; }
  .card-back .brand-name { color: var(--ink); font-size: 20px; }
  .person-name {
    font-family: "Open Sans", sans-serif; font-weight: 400;
    font-size: 25px; color: var(--ink); margin-top: 24px;
  }
  .contact-line {
    display: flex; align-items: center; gap: 10px;
    font-family: "Open Sans", sans-serif; font-size: 18px; color: var(--ink-soft);
    margin-top: 14px;
  }
  .contact-line svg { width: 16px; height: 16px; fill: var(--ink-soft); }
  .web-band {
    position: absolute; left: 0; bottom: 0; width: 100%; height: 19%;
    background: linear-gradient(180deg, #4a4b4d 0%, var(--card-black) 100%);
    display: flex; align-items: center; justify-content: center; gap: 12px;
    font-family: "Open Sans", sans-serif; font-size: 18px; color: #e6e6e6;
  }
  .web-band svg { width: 16px; height: 16px; }
</style>
</head>
<body>
<main class="canvas">

  <section class="card card-front" aria-label="Card front">
    <div class="world-map" role="img" aria-label="Faint dark world map across the upper card"></div>
    <div class="front-brand">
      <span class="brand-dot"></span>
      <div class="brand-name">Tallowbrook<br>Migration</div>
    </div>
    <div class="red-band"></div>
  </section>

  <section class="card card-back" aria-label="Card back">
    <div class="back-content">
      <span class="brand-dot"></span>
      <div class="brand-name">Tallowbrook<br>Migration</div>
      <p class="person-name">Marla Voskuil, RCIC</p>
      <p class="contact-line">
        <svg viewBox="0 0 24 24" aria-hidden="true"><path d="M6.6 10.8a15 15 0 0 0 6.6 6.6l2.2-2.2a1 1 0 0 1 1-.25 11.4 11.4 0 0 0 3.6.57 1 1 0 0 1 1 1V20a1 1 0 0 1-1 1A17 17 0 0 1 3 4a1 1 0 0 1 1-1h3.5a1 1 0 0 1 1 1c0 1.25.2 2.45.57 3.57a1 1 0 0 1-.25 1z"/></svg>
        (604) 731-5562
      </p>
      <p class="contact-line">
        <svg viewBox="0 0 24 24" aria-hidden="true"><path d="M2 5h20v14H2z M2 5l10 8 10-8" fill="none" stroke="#3a3a3a" stroke-width="2"/></svg>
        marla@tallowbrookmigration.example
      </p>
    </div>
    <div class="web-band">
      <svg viewBox="0 0 24 24" aria-hidden="true"><circle cx="12" cy="12" r="9" fill="none" stroke="#e6e6e6" stroke-width="2"/><path d="M3 12h18M12 3c3 3 3 15 0 18M12 3c-3 3-3 15 0 18" fill="none" stroke="#e6e6e6" stroke-width="1.6"/></svg>
      www.tallowbrookmigration.example
    </div>
  </section>

</main>
</body>
</html>
```